Dental office stationary (letterhead, envelopes), business cards, presentation folders

Nothing too dental outside of the logo. I will need all stationary, presentation folders, business cards. Would prefer to stay in the colors of the logo

Gordon Plaskett, DDS
Brightvale Dental Implant Center
772-555-0187
info@brightvaledental-example.com
3875 NW Orchard Pkwy Unit B
Stuart, FL 34917

Also need appointment date and time
And cancellation policy
I want it to say “kindly ask for
A 48hr cancellation policy to avoid incurring a cancellation fee”

Dental

Colors
0054AA
0677BA
7BADD7
CADEEF
E8F1F8

Requirements
Must have
• Name of your office, name of doctor, address, phone number
Should not have
• Too much tooth/dental. Only the tooth in logo

```html
<!DOCTYPE html>
<html lang="en">
<head>
<meta charset="utf-8">
<title>Brightvale Dental Implant Center – Stationery</title>
<link href="https://fonts.googleapis.com/css2?family=Roboto:wght@400;500;700&display=swap" rel="stylesheet">
<style>
  :root{
    --bg:#cbcbcb;
    --brand:#0d65b3;
    --brand-deep:#0054aa;
    --brand-mid:#0677ba;
    --teal:#1db99a;
    --paper:#ffffff;
    --ink:#333333;
    --ink-soft:#555555;
    --rule:#8a8a8a;
  }
  *{box-sizing:border-box;margin:0;padding:0}
  html,body{width:1200px;height:1011px;overflow:hidden}
  body{position:relative;background:var(--bg);font-family:'Roboto',Arial,sans-serif;color:var(--ink)}
  .piece{position:absolute;background:var(--paper);box-shadow:0 2px 5px rgba(0,0,0,.28);overflow:hidden}

  /* wordmark */
  .wordmark{text-align:center;font-weight:400;color:var(--brand-mid);line-height:1}
  .wordmark .name{display:block;letter-spacing:.02em}
  .wordmark .tag{display:block;text-transform:uppercase;letter-spacing:.28em}
  .wordmark.on-dark{color:#fff}

  /* business card */
  .biz-card{left:53px;top:98px;width:325px;height:186px;border-radius:14px;background:var(--brand)}
  .biz-card svg{position:absolute;inset:0}
  .biz-card .doctor{position:absolute;left:16px;top:36px;color:#fff;font-weight:700;font-size:11px}
  .biz-card .address{position:absolute;left:16px;top:78px;color:#fff;font-size:8.4px;line-height:11px}
  .biz-card .contact{position:absolute;left:16px;top:118px;color:#fff;font-size:7.8px;line-height:10.8px}
  .contact-row{display:flex;align-items:center;gap:3px;white-space:nowrap}
  .contact-row svg{position:static;width:7px;height:7px;flex:none}
  .biz-card .wordmark{position:absolute;left:172px;top:78px;width:148px}
  .biz-card .name{font-size:20px}
  .biz-card .tag{font-size:5.2px;margin-top:3px}

  /* appointment card */
  .appt-card{left:53px;top:315px;width:325px;height:186px;border-radius:14px}
  .appt-card .band{position:absolute;left:0;top:0;width:100%;height:66px;background:var(--brand)}
  .appt-card .band-line{position:absolute;left:0;top:68px;width:100%;height:3px;background:var(--teal)}
  .appt-card .tab{position:absolute;left:84px;top:68px;width:157px;height:13px;background:var(--teal);clip-path:polygon(0 0,100% 0,88% 100%,12% 100%);color:#fff;font-size:11.5px;text-align:center;line-height:14px}
  .appt-card .wordmark{position:absolute;left:60px;top:27px;width:205px}
  .appt-card .name{font-size:22px}
  .appt-card .tag{font-size:6px;margin-top:3px}
  .appt-card .dash{position:absolute;left:21px;right:21px;top:109px;border-top:1px dashed #9a9a9a}
  .appt-card .fields{position:absolute;left:21px;right:21px;top:127px;display:flex;align-items:flex-end;font-size:9.4px;color:var(--ink-soft);gap:3px}
  .appt-card .fill{flex:1;border-bottom:1px solid #777;height:8px}
  .appt-card .fill.short{flex:.75}
  .appt-card .policy{position:absolute;left:0;right:0;top:152px;text-align:center;font-size:8.7px;line-height:10.5px;color:var(--ink-soft)}
  .appt-card .policy b{color:var(--ink)}

  /* letterhead */
  .letterhead{left:402px;top:97px;width:286px;height:404px}
  .letterhead .wordmark{position:absolute;left:18px;top:31px;width:105px}
  .letterhead .name{font-size:15px}
  .letterhead .tag{font-size:4.4px;margin-top:2px}
  .letterhead .head-contact{position:absolute;left:203px;top:19px;font-size:4.6px;line-height:6px;color:var(--ink-soft)}
  .letterhead .head-contact .gap{height:3px}
  .letterhead .head-contact .contact-row{gap:2px}
  .letterhead .head-contact svg{width:4px;height:4px}
  .letterhead .head-contact .web{color:var(--teal)}
  .letterhead .rule{position:absolute;left:20px;right:20px;top:55px;border-top:1px solid var(--rule)}
  .letterhead .salutation{position:absolute;left:26px;top:124px;font-size:6.5px;font-weight:500}
  .letterhead .body{position:absolute;left:26px;right:26px;top:142px;font-size:4.5px;line-height:5.9px;color:var(--ink-soft)}
  .letterhead .body p{margin-bottom:5px}
  .letterhead .closing{position:absolute;left:26px;top:263px;font-size:4px}
  .letterhead .signature{position:absolute;left:27px;top:280px;width:36px;height:10px;background:linear-gradient(90deg,#6d6d6d,#9a9a9a);border-radius:5px;opacity:.55}

  /* envelope front */
  .envelope-front{left:715px;top:98px;width:431px;height:188px}
  .envelope-front .wordmark{position:absolute;left:15px;top:24px;width:88px}
  .envelope-front .name{font-size:13px}
  .envelope-front .tag{font-size:3.7px;margin-top:2px}
  .envelope-front .return{position:absolute;left:15px;top:48px;font-size:6.3px;line-height:8px;color:var(--ink-soft)}

  /* envelope back */
  .envelope-back{left:713px;top:312px;width:435px;height:189px}
  .envelope-back .flap{position:absolute;left:0;top:0;width:100%;height:52px}
  .envelope-back .wordmark{position:absolute;left:167px;top:20px;width:100px}
  .envelope-back .name{font-size:15px}
  .envelope-back .tag{font-size:4.2px;margin-top:2px}

  /* folder outside spread */
  .folder-outside{left:55px;top:575px;width:525px;height:400px;background:var(--brand);display:flex}
  .folder-outside .panel{position:relative;flex:1}
  .folder-outside .panel + .panel{border-left:1px solid rgba(0,0,0,.15);background:linear-gradient(160deg,#1a74c2 0%,var(--brand) 45%,#0a5ca6 100%)}
  .folder-outside .back-contact{position:absolute;left:18px;right:18px;bottom:18px;color:#fff;font-size:6px;line-height:9px}
  .folder-outside .back-contact .contact-row{gap:3px}
  .folder-outside .back-contact .contact-row svg{width:5px;height:5px}
  .folder-outside .back-contact .rule{border-top:1px solid rgba(255,255,255,.7);width:200px;margin-top:3px}
  .folder-outside .wordmark{position:absolute;left:21px;top:162px;width:220px}
  .folder-outside .name{font-size:28px}
  .folder-outside .tag{font-size:7px;margin-top:5px}

  /* folder inside spread */
  .folder-inside{left:620px;top:575px;width:525px;height:400px;display:flex;background:transparent;box-shadow:none}
  .folder-inside .panel{position:relative;flex:1;background:linear-gradient(180deg,#f4f4f4,#e6e6e6);box-shadow:0 2px 5px rgba(0,0,0,.28)}
  .folder-inside .panel + .panel{border-left:1px solid #cfcfcf;background:linear-gradient(180deg,#fafafa,#ececec)}
  .folder-inside .pocket{position:absolute;left:0;right:0;bottom:0;height:118px;background:var(--brand);border-top:2px solid rgba(255,255,255,.6)}
</style>
</head>
<body>

<section class="piece biz-card" aria-label="Business card">
  <svg viewBox="0 0 325 186" width="325" height="186" aria-hidden="true">
    <circle cx="343" cy="93" r="190" fill="none" stroke="var(--teal)" stroke-width="3"/>
    <circle cx="345" cy="93" r="186" fill="#fff"/>
  </svg>
  <p class="doctor">Gordon Plaskett, DDS</p>
  <p class="address">3875 NW Orchard Pkwy Unit B<br>Stuart, FL 34917</p>
  <div class="contact">
    <p class="contact-row"><svg viewBox="0 0 10 10"><path d="M2 1h2l1 2.5-1.3 1a6 6 0 0 0 2.8 2.8l1-1.3L10 7v2c0 .6-.4 1-1 1A9 9 0 0 1 0 2c0-.6.4-1 1-1z" fill="#fff"/></svg>772-555-0187</p>
    <p class="contact-row"><svg viewBox="0 0 10 10"><rect x="0.5" y="2" width="9" height="6.5" rx="1" fill="#fff"/><path d="M1 2.5l4 3 4-3" stroke="var(--brand)" fill="none" stroke-width="1"/></svg>info@brightvaledental-example.com</p>
    <p class="contact-row"><svg viewBox="0 0 10 10"><circle cx="5" cy="5" r="4.5" fill="#fff"/><path d="M5 .5v9M.5 5h9M2 2.5q3 1.5 6 0M2 7.5q3-1.5 6 0" stroke="var(--brand)" fill="none" stroke-width=".7"/></svg>www.brightvaledental-example.com</p>
  </div>
  <div class="wordmark"><span class="name">Brightvale</span><span class="tag">Dental Implant Center</span></div>
</section>

<section class="piece appt-card" aria-label="Appointment card">
  <div class="band"></div>
  <div class="wordmark on-dark"><span class="name">Brightvale</span><span class="tag">Dental Implant Center</span></div>
  <div class="band-line"></div>
  <div class="tab">APPOINTMENT</div>
  <div class="dash"></div>
  <div class="fields"><span>DATE :</span><span class="fill"></span><span>TIME :</span><span class="fill short"></span></div>
  <p class="policy">If you are unable to keep this appointment please notify us at least<br><b>48 hours</b> in advance to avoid a broken appointment charge</p>
</section>

<section class="piece letterhead" aria-label="Letterhead">
  <div class="wordmark"><span class="name">Brightvale</span><span class="tag">Dental Implant Center</span></div>
  <div class="head-contact">
    <p>3875 NW Orchard Pkwy Unit B</p>
    <p>Stuart, FL 34917</p>
    <div class="gap"></div>
    <p class="contact-row"><svg viewBox="0 0 10 10"><path d="M2 1h2l1 2.5-1.3 1a6 6 0 0 0 2.8 2.8l1-1.3L10 7v2c0 .6-.4 1-1 1A9 9 0 0 1 0 2c0-.6.4-1 1-1z" fill="var(--teal)"/></svg>772-555-0187</p>
    <p class="contact-row"><svg viewBox="0 0 10 10"><rect x="0.5" y="2" width="9" height="6.5" rx="1" fill="var(--teal)"/></svg>info@brightvaledental-example.com</p>
    <p class="contact-row"><svg viewBox="0 0 10 10"><circle cx="5" cy="5" r="4.5" fill="var(--teal)"/></svg><span>www.<span class="web">brightvaledental-example</span>.com</span></p>
  </div>
  <div class="rule"></div>
  <p class="salutation">Dear Mr. Hallworth,</p>
  <div class="body">
    <p>Thank you for choosing our practice for your implant care. This letter confirms the details of your upcoming consultation and explains what to expect during the visit. Please bring a list of current medications, your insurance card and any recent dental records or x-rays you may have.</p>
    <p>During the first appointment our team will review your history, take new images and discuss every treatment option with you. We will answer your questions and prepare a clear written plan with costs and timing.</p>
    <p>Most patients return home the same day and resume normal activity within a short time. Our staff will call after each procedure to check on your comfort and recovery, and we remain available by phone for any concern between visits.</p>
    <p>We look forward to meeting you and helping you regain a confident, comfortable smile. Please contact our office if you need to change your appointment time.</p>
  </div>
  <p class="closing">Sincerely,</p>
  <div class="signature" role="img" aria-label="Handwritten signature"></div>
</section>

<section class="piece envelope-front" aria-label="Envelope front">
  <div class="wordmark"><span class="name">Brightvale</span><span class="tag">Dental Implant Center</span></div>
  <p class="return">3875 NW Orchard Pkwy Unit B<br>Stuart, FL 34917</p>
</section>

<section class="piece envelope-back" aria-label="Envelope back">
  <svg class="flap" viewBox="0 0 435 52" preserveAspectRatio="none" aria-hidden="true">
    <path d="M0 0H435L425 38Q421 52 405 52H30Q14 52 10 38Z" fill="var(--brand)"/>
  </svg>
  <div class="wordmark on-dark"><span class="name">Brightvale</span><span class="tag">Dental Implant Center</span></div>
</section>

<section class="piece folder-outside" aria-label="Presentation folder outside">
  <div class="panel">
    <div class="back-contact">
      <p>3875 NW Orchard Pkwy Unit B, Stuart, FL 34917</p>
      <p class="contact-row"><svg viewBox="0 0 10 10"><path d="M2 1h2l1 2.5-1.3 1a6 6 0 0 0 2.8 2.8l1-1.3L10 7v2c0 .6-.4 1-1 1A9 9 0 0 1 0 2c0-.6.4-1 1-1z" fill="#fff"/></svg>772-555-0187 &nbsp;<svg viewBox="0 0 10 10"><rect x="0.5" y="2" width="9" height="6.5" rx="1" fill="#fff"/></svg>info@brightvaledental-example.com</p>
      <p class="contact-row"><svg viewBox="0 0 10 10"><circle cx="5" cy="5" r="4.5" fill="#fff"/></svg>www.brightvaledental-example.com</p>
      <div class="rule"></div>
    </div>
  </div>
  <div class="panel">
    <div class="wordmark on-dark"><span class="name">Brightvale</span><span class="tag">Dental Implant Center</span></div>
  </div>
</section>

<section class="piece folder-inside" aria-label="Presentation folder inside">
  <div class="panel"><div class="pocket"></div></div>
  <div class="panel"><div class="pocket"></div></div>
</section>

</body>
</html>
```